Business Cards

Business cards (double-sided) to be handed out to clients and potential clients, with contact details, logo .

Target Market(s)

Small to medium size businesses

Industry/Entity Type

Accountants

Contact Information for Business Card

Brightwater Ledger & Counsel Ltd

Colors

Designer to choose only greyscale colors for use in the design.

Requirements
Must have
• Name, Title, Address, Phone number, Email, Website
Nice to have
• Modern, clean lines, classy
Should not have
• Business cards to be double-sided. Form keeps reverting to single-sided.

```html
<!DOCTYPE html>
<html lang="en">
<head>
<meta charset="utf-8">
<title>Brightwater Ledger & Counsel — Business Cards</title>
<link href="https://fonts.googleapis.com/css2?family=Jost:wght@400;500&family=Roboto:wght@400&display=swap" rel="stylesheet">
<style>
  :root {
    --backdrop: #2a2a2b;
    --card: #1c1c1e;
    --ink-light: #d9d9d9;
    --ink-deboss: #4a4a4d;
  }
  * { margin: 0; padding: 0; box-sizing: border-box; }
  html, body { width: 1200px; height: 1138px; overflow: hidden; background: var(--backdrop); }
  .canvas { position: relative; width: 1200px; height: 1138px; }

  .card {
    position: absolute;
    left: 273px;
    width: 621px;
    height: 376px;
    background: var(--card);
    border-radius: 16px;
    overflow: hidden;
  }
  .card--front { top: 184px; }
  .card--back { top: 606px; display: flex; align-items: center; justify-content: center; }

  /* front side is set in portrait and turned to read bottom-to-top */
  .front-layout {
    position: absolute;
    left: 122.5px;
    top: -122.5px;
    width: 376px;
    height: 621px;
    transform: rotate(-90deg);
    color: var(--ink-light);
    text-align: center;
  }
  .brand {
    position: absolute;
    top: 100px;
    left: 0; right: 0;
    display: flex; align-items: center; justify-content: center; gap: 12px;
    font-family: "Jost", sans-serif;
    font-weight: 400;
    font-size: 26px;
    line-height: 1.25;
    text-align: left;
  }
  .brand__square { width: 12px; height: 12px; background: var(--ink-light); flex: none; }

  .person { position: absolute; top: 306px; left: 0; right: 0; }
  .person__name { font-family: "Jost", sans-serif; font-weight: 500; font-size: 21px; line-height: 1.15; }
  .person__title { font-family: "Roboto", sans-serif; font-size: 14px; }

  .divider { position: absolute; top: 393px; left: 0; width: 376px; height: 3px; }
  .icons { position: absolute; top: 383px; left: 0; right: 0; display: flex; justify-content: center; gap: 4px; }
  .icons svg { width: 21px; height: 21px; }

  .contact { position: absolute; top: 414px; left: 0; right: 0; font-family: "Roboto", sans-serif; font-size: 14.5px; line-height: 21px; }
  .address { position: absolute; top: 497px; left: 0; right: 0; font-family: "Roboto", sans-serif; font-size: 14.5px; line-height: 21px; }

  .brand--back {
    display: flex; align-items: center; gap: 14px;
    font-family: "Jost", sans-serif;
    font-weight: 400;
    font-size: 36px;
    line-height: 1.2;
    color: var(--ink-deboss);
    transform: translateY(-12px);
  }
  .brand--back .brand__square { width: 18px; height: 18px; background: var(--ink-deboss); flex: none; }
</style>
</head>
<body>
<main class="canvas">
  <section class="card card--front" aria-label="Business card front">
    <div class="front-layout">
      <div class="brand">
        <span class="brand__square"></span>
        <span class="brand__name">Brightwater<br>Ledger &amp; Counsel</span>
      </div>

      <div class="person">
        <p class="person__name">Daniel Marsh</p>
        <p class="person__title">Managing Director</p>
      </div>

      <svg class="divider" viewBox="0 0 376 3" aria-hidden="true">
        <path d="M58 1.5 L128 1.5" stroke="#d9d9d9" stroke-width="1.5" stroke-linecap="round"/>
        <path d="M244 1.5 L316 1.5" stroke="#d9d9d9" stroke-width="1.5" stroke-linecap="round"/>
      </svg>
      <div class="icons" aria-hidden="true">
        <svg viewBox="0 0 20 20"><circle cx="10" cy="10" r="9" fill="none" stroke="#d9d9d9" stroke-width="1.2"/><path d="M6.5 6 C6.5 11 9 13.5 14 13.5 L14 11.8 L12 11 L11 12 C9.5 11.3 8.7 10.5 8 9 L9 8 L8.2 6 Z" fill="#d9d9d9"/></svg>
        <svg viewBox="0 0 20 20"><circle cx="10" cy="10" r="9" fill="none" stroke="#d9d9d9" stroke-width="1.2"/><rect x="5.5" y="7" width="9" height="6.5" fill="none" stroke="#d9d9d9" stroke-width="1.1"/><path d="M5.5 7 L10 10.8 L14.5 7" fill="none" stroke="#d9d9d9" stroke-width="1.1"/></svg>
        <svg viewBox="0 0 20 20"><circle cx="10" cy="10" r="9" fill="none" stroke="#d9d9d9" stroke-width="1.2"/><circle cx="10" cy="10" r="4.8" fill="none" stroke="#d9d9d9" stroke-width="1"/><ellipse cx="10" cy="10" rx="2" ry="4.8" fill="none" stroke="#d9d9d9" stroke-width="1"/><path d="M5.2 10 H14.8" stroke="#d9d9d9" stroke-width="1"/></svg>
      </div>

      <div class="contact">
        <p>555-014-2273</p>
        <p>daniel@brightwaterledger.com</p>
        <p>www.brightwaterledger.com</p>
      </div>
      <div class="address">
        <p>58 Harbour Lane, Eastmere,</p>
        <p>Northvale, US 482190</p>
      </div>
    </div>
  </section>

  <section class="card card--back" aria-label="Business card back">
    <div class="brand--back">
      <span class="brand__square"></span>
      <span class="brand__name">Brightwater Ledger &amp; Counsel</span>
    </div>
  </section>
</main>
</body>
</html>
```